Now Leasing Banner

Looking for a banner that says the following information approx 4' x 30'

Now Leasing Maplewood Terrace 925-318-6054

Target Market(s)

Drive by traffic

Industry/Entity Type

Residential property management

Requirements
Must have
• Clear and readable from a distance

```html
<!DOCTYPE html>
<html lang="en">
<head>
<meta charset="utf-8">
<title>Now Leasing Banner – Maplewood Terrace</title>
<link rel="stylesheet" href="https://fonts.googleapis.com/css2?family=Montserrat:wght@400;700;900&display=swap">
<style>
  :root {
    --banner-teal: #135b66;
    --banner-white: #fbfbfb;
  }
  html, body {
    margin: 0;
    padding: 0;
    width: 1200px;
    height: 160px;
    overflow: hidden;
    background: var(--banner-teal);
  }
  .banner {
    display: block;
    width: 1200px;
    height: 160px;
  }
  .banner-bg { fill: var(--banner-teal); }
  .headline {
    font-family: "Montserrat", sans-serif;
    font-weight: 900;
    font-size: 106px;
    fill: var(--banner-white);
  }
  .rule { fill: var(--banner-white); }
  .property-name {
    font-family: "Montserrat", sans-serif;
    font-weight: 400;
    font-size: 27px;
    letter-spacing: 7px;
    fill: var(--banner-white);
  }
  .phone {
    font-family: "Montserrat", sans-serif;
    font-weight: 700;
    font-size: 27px;
    fill: var(--banner-white);
  }
</style>
</head>
<body>
<svg class="banner" viewBox="0 0 1200 160" xmlns="http://www.w3.org/2000/svg" role="img" aria-label="Now Leasing – Maplewood Terrace – 925-318-6054">
  <rect class="banner-bg" x="0" y="0" width="1200" height="160"/>
  <text class="headline" x="50" y="93" textLength="1110" lengthAdjust="spacing">NOW LEASING</text>
  <rect class="rule" x="50" y="105.5" width="1110" height="2.2"/>
  <text class="property-name" x="575" y="143" text-anchor="end">MAPLEWOOD TERRACE</text>
  <rect class="rule" x="598.5" y="117" width="2.6" height="34"/>
  <text class="phone" x="632" y="143" textLength="266" lengthAdjust="spacing">925-318-6054</text>
</svg>
</body>
</html>
```